KVRo Business Cards

We need a business card design. We are a Technology (Audio Visual) design, sales and installation company. Looking for a double sided design, clean

Contact Information for Business Card

Clean, modern look, 2 sided

Font styles to use
Sans Serif

```html
<!DOCTYPE html>
<html lang="en">
<head>
<meta charset="utf-8">
<title>KVRo Business Cards</title>
<link rel="stylesheet" href="https://fonts.googleapis.com/css2?family=Arimo:wght@400;700&display=swap">
<style>
  :root {
    --stage: #1c1c1c;
    --card: #222222;
    --card-edge: #f39a2b;
    --accent: #f39a2b;
    --ink: #ffffff;
    --silver: #b9babd;
  }
  * { margin: 0; padding: 0; box-sizing: border-box; }
  html, body {
    width: 1200px;
    height: 900px;
    overflow: hidden;
    background: var(--stage);
    font-family: "Arimo", Arial, sans-serif;
  }
  .sheet {
    position: relative;
    width: 1200px;
    height: 900px;
  }
  .card {
    position: absolute;
    left: 290px;
    width: 620px;
    height: 354px;
    background: var(--card);
    border-right: 2px solid var(--card-edge);
    border-bottom: 2px solid var(--card-edge);
    box-shadow: 0 14px 30px rgba(0, 0, 0, 0.55);
  }
  .card--front { top: 60px; }
  .card--back { top: 486px; }

  .wordmark {
    font-weight: 700;
    letter-spacing: -2px;
    line-height: 1;
    position: absolute;
    left: 0;
    right: 0;
    text-align: center;
  }
  .card--front .wordmark {
    top: 118px;
    font-size: 112px;
    color: var(--silver);
  }
  .card--back .wordmark {
    top: 34px;
    font-size: 100px;
    color: var(--ink);
  }

  .identity {
    position: absolute;
    top: 168px;
    right: 346px;
    text-align: right;
  }
  .identity__name {
    color: var(--accent);
    font-weight: 700;
    font-size: 29px;
    letter-spacing: 0.5px;
    text-transform: uppercase;
  }
  .identity__role {
    color: var(--ink);
    font-size: 19px;
    margin-top: 6px;
  }
  .divider {
    position: absolute;
    left: 292px;
    top: 166px;
    width: 3px;
    height: 96px;
    background: var(--accent);
  }
  .contacts {
    position: absolute;
    left: 314px;
    top: 166px;
    list-style: none;
  }
  .contacts__item {
    display: flex;
    align-items: center;
    gap: 9px;
    color: var(--ink);
    font-size: 18px;
    height: 25px;
  }
  .contacts__icon {
    width: 14px;
    height: 14px;
    fill: var(--accent);
    flex: none;
  }
  .address {
    position: absolute;
    left: 50px;
    bottom: 34px;
    color: var(--ink);
    font-size: 17px;
  }
  .address__label { color: var(--accent); }
</style>
</head>
<body>
<main class="sheet">
  <section class="card card--front" aria-label="Card front">
    <div class="wordmark">KVRo</div>
  </section>

  <section class="card card--back" aria-label="Card back">
    <div class="wordmark">KVRo</div>

    <div class="identity">
      <div class="identity__name">Dana Whitlock</div>
      <div class="identity__role">President, CEO</div>
    </div>

    <div class="divider"></div>

    <ul class="contacts">
      <li class="contacts__item">
        <svg class="contacts__icon" viewBox="0 0 16 16" aria-hidden="true"><path d="M3.6 1.2l2.2 2.6c.3.4.3.9 0 1.2L4.6 6.3c.9 2 2.9 4 5 5l1.3-1.2c.3-.3.9-.3 1.2 0l2.6 2.2c.4.3.4.9.1 1.2l-1.5 1.5c-.5.5-1.3.6-2 .3C6.6 13.5 2.5 9.4.7 4.7.4 4 .5 3.2 1 2.7L2.4 1.2c.3-.4.9-.4 1.2 0z"/></svg>
        <span>555-310-2847</span>
      </li>
      <li class="contacts__item">
        <svg class="contacts__icon" viewBox="0 0 16 16" aria-hidden="true"><path d="M4.5 0h7c.8 0 1.5.7 1.5 1.5v13c0 .8-.7 1.5-1.5 1.5h-7C3.7 16 3 15.3 3 14.5v-13C3 .7 3.7 0 4.5 0zm.5 2v10h6V2H5zm3 11a1 1 0 100 2 1 1 0 000-2z"/></svg>
        <span>555-610-7734</span>
      </li>
      <li class="contacts__item">
        <svg class="contacts__icon" viewBox="0 0 16 16" aria-hidden="true"><path d="M0 3h16v1.2L8 9 0 4.2V3zm0 2.6l8 4.8 8-4.8V13H0V5.6z"/></svg>
        <span>hello@kvroav.com</span>
      </li>
      <li class="contacts__item">
        <svg class="contacts__icon" viewBox="0 0 16 16" aria-hidden="true"><path d="M8 0a8 8 0 110 16A8 8 0 018 0zm-.9 1.6C4.5 2 2.3 4 1.7 6.6l2.6 1.2.9 2.2-.8 1.6.8 2.2c.7.4 1.5.6 2.3.7l.3-2.6 1.6-1.4-.8-2-2.3-.4-.8-1.6 1.2-1.5 1.1-.4-.7-3zm2.6.2l.6 1.6 2.2.8.8 2.4 1.5.6A6.5 6.5 0 009.7 1.8z"/></svg>
        <span>www.kvroav.com</span>
      </li>
    </ul>

    <p class="address"><span class="address__label">Address</span> : 742 Harbor Lane, STE 210 Oakridge, CA 90000</p>
  </section>
</main>
</body>
</html>
```